Design AND code an HTML landing page

A landing page for campaigns and webinars respondents for project www.brevoa-homes.com. We expect the design to be coded. We will provide the copy and content. It will be a simple landing page for a new development project, to capture details of any potential clients showing interest, including any leads generated via webinars.

Broad instructions are as follows:
- It should not have a header or footer. Minimum escape links as possible.
- Create a lead generator box to get e-mails / relevant info of people interested.
- If possible, add a virtual tour (link to host server provided) at the top of the page.
- Content will be provided
- An option to include a link to a ClipHarbor video

Target Market(s)

Pre/retiree and retirees

Industry/Entity Type

Real estate development, retirement, relocation, travel and tourism

Coding

Coded - Design and coding required

Font styles to use
Other font styles liked:
• Preferably same as existing site

Colors
FFF300
FFF600
FEFA6F
FFFEC7
FFFEE8

Requirements
Must have
• Simple yet appealing look and feel, within the motif of the project, simple list of questions
Should not have
• Emojis, unrelated graphics, excessive graphics that are not linked to project

```html
<!DOCTYPE html>
<html lang="en">
<head>
<meta charset="utf-8">
<title>Brevoa Homes – Landing Page Variants</title>
<link rel="stylesheet" href="https://fonts.googleapis.com/css2?family=Montserrat:wght@400;500;600&family=Arimo:wght@400&display=swap">
<style>
  :root {
    --canvas: #ececec;
    --yellow: #fff300;
    --yellow-deep: #f3d91a;
    --ink: #2a2a2a;
    --footer: #232323;
    --white: #ffffff;
    --field-text: #444444;
  }
  * { box-sizing: border-box; margin: 0; padding: 0; }
  html, body {
    width: 1200px; height: 784px; overflow: hidden;
    background: var(--canvas);
  }
  body { position: relative; font-family: "Arimo", Arial, sans-serif; }

  .page {
    position: absolute; top: 32px;
    width: 555px; height: 704px;
    display: flex; flex-direction: column;
    background: var(--white);
    box-shadow: 0 1px 4px rgba(0,0,0,0.08);
    overflow: hidden;
  }
  .page--a { left: 26px; }
  .page--b { left: 608px; }

  /* Hero */
  .hero {
    position: relative; height: 316px; flex: none;
    background:
      linear-gradient(rgba(20,22,24,0.45), rgba(20,22,24,0.5)),
      linear-gradient(180deg, #5a6470 0%, #4d4a44 35%, #5c5a4d 58%, #56603a 78%, #3f4a2c 100%);
    color: var(--white);
    text-align: center;
  }
  .brand {
    position: absolute; left: 51px; top: 21px;
    font-family: "Montserrat", sans-serif; font-weight: 400;
    font-size: 18px; line-height: 22px; color: var(--white); letter-spacing: 0.2px;
  }
  .menu-toggle {
    position: absolute; left: 472px; top: 16px;
    width: 31px; height: 31px; border-radius: 50%;
    border: 1.5px solid var(--yellow);
    background: rgba(0,0,0,0.35);
    display: flex; align-items: center; justify-content: center;
  }
  .hero__title {
    position: absolute; left: 0; right: 0; top: 128px;
    font-family: "Montserrat", sans-serif; font-weight: 500;
    font-size: 19px; letter-spacing: 0.3px;
  }
  .hero__text {
    position: absolute; left: 0; right: 0; top: 156px;
    font-size: 8.4px; line-height: 14px;
  }
  .btn {
    display: inline-flex; align-items: center; justify-content: center;
    font-family: "Montserrat", sans-serif; font-weight: 500;
    border-radius: 14px; letter-spacing: 0.2px;
  }
  .btn--tour {
    position: absolute; left: 228px; top: 208px;
    width: 99px; height: 28px;
    color: var(--white);
    font-size: 9px; font-weight: 600;
    background: linear-gradient(#fff300, #f5e400);
  }

  /* Videos */
  .videos {
    height: 215px; flex: none;
    padding-top: 30px;
    display: flex; justify-content: center; gap: 16px;
    background: var(--white);
  }
  .video {
    position: relative; width: 218px; height: 153px;
    overflow: hidden;
  }
  .video__frame { position: absolute; inset: 0 0 12px 0; }
  .video__frame--aerial {
    background: linear-gradient(160deg, #7f9460 0%, #5c6b45 35%, #4a4a40 60%, #6c8a7a 80%, #b7aa98 100%);
  }
  .video__frame--terrace {
    background: linear-gradient(180deg, #a9c7e2 0%, #c6dbec 38%, #7c8d8e 52%, #7a7f84 70%, #9c9ea0 100%);
  }
  .video__play {
    position: absolute; left: 50%; top: 70px;
    width: 32px; height: 22px; margin-left: -16px;
    border-radius: 6px; background: rgba(30,30,30,0.75);
    display: flex; align-items: center; justify-content: center;
  }
  .video__bar {
    position: absolute; left: 0; right: 0; bottom: 0; height: 12px;
    background: #151515; color: #cfcfcf;
    font-size: 4px; display: flex; align-items: center; padding: 0 6px; gap: 8px;
  }
  .video__bar::before {
    content: ""; position: absolute; left: 0; right: 0; top: -2px; height: 2px;
    background: #8a8a8a;
  }
  .video__time { margin-left: 4px; }
  .video__host { margin-left: auto; }

  /* Lead form */
  .lead {
    position: relative; height: 134px; flex: none;
    padding-top: 23px;
    background: linear-gradient(180deg, #f6de1c 0%, #f2d810 55%, #ecd20c 100%);
  }
  .lead__row {
    display: flex; justify-content: center; gap: 7px; margin-bottom: 10px;
  }
  .field {
    height: 23px; background: var(--white);
    font-family: "Montserrat", sans-serif; font-size: 7px; color: var(--field-text);
    display: flex; align-items: center; padding-left: 7px;
  }
  .field--third { width: 124px; }
  .field--half { width: 189px; }
  .btn--submit {
    display: flex; margin: 4px auto 0;
    width: 93px; height: 27px;
    background: var(--ink); color: var(--white);
    font-size: 8px;
  }

  /* Footer */
  .footer {
    height: 39px; flex: none; background: var(--footer);
    color: var(--white); font-size: 7.2px;
    display: flex; align-items: center; justify-content: center;
  }
</style>
</head>
<body>

  <main class="page page--a">
    <section class="hero" role="img" aria-label="Photo of a modern apartment building with balconies and a garden where residents walk">
      <div class="brand">Brevoa Homes</div>
      <div class="menu-toggle">
        <svg width="9" height="8" viewBox="0 0 9 8"><rect y="0" width="9" height="1.5" fill="#fff"/><rect y="3.2" width="9" height="1.5" fill="#fff"/><rect y="6.4" width="9" height="1.5" fill="#fff"/></svg>
      </div>
      <h1 class="hero__title">REINVENTING RETIREMENT</h1>
      <p class="hero__text">The retirement village concept is still in its infancy in Southern Europe.<br>Retirement villages in North America, Australia and South Africa, for<br>example, have existed for some time.</p>
      <a class="btn btn--tour">VIRTUAL TOUR</a>
    </section>

    <section class="videos">
      <div class="video">
        <div class="video__frame video__frame--aerial" role="img" aria-label="Aerial render of the development with pool and gardens"></div>
        <div class="video__play"><svg width="10" height="10" viewBox="0 0 10 10"><path d="M2 1 L9 5 L2 9 Z" fill="#fff"/></svg></div>
        <div class="video__bar"><span>▶</span><span class="video__time">0:00 / 3:00</span><span class="video__host">ClipHarbor</span></div>
      </div>
      <div class="video">
        <div class="video__frame video__frame--terrace" role="img" aria-label="Render of a rooftop terrace with sun loungers and sea view"></div>
        <div class="video__play"><svg width="10" height="10" viewBox="0 0 10 10"><path d="M2 1 L9 5 L2 9 Z" fill="#fff"/></svg></div>
        <div class="video__bar"><span>▶</span><span class="video__time">0:00 / 3:00</span><span class="video__host">ClipHarbor</span></div>
      </div>
    </section>

    <section class="lead">
      <div class="lead__row">
        <div class="field field--third">Name :</div>
        <div class="field field--third">Email :</div>
        <div class="field field--third">Phone :</div>
      </div>
      <div class="lead__row">
        <div class="field field--half">Interest :</div>
        <div class="field field--half">Comment :</div>
      </div>
      <a class="btn btn--submit">SUBMIT</a>
    </section>

    <footer class="footer">© Copyright 2022 Brevoa Homes.All Rights Reserved</footer>
  </main>

  <main class="page page--b">
    <section class="hero" role="img" aria-label="Photo of a modern apartment building with balconies and a garden where residents walk">
      <div class="brand">Brevoa Homes</div>
      <div class="menu-toggle">
        <svg width="9" height="8" viewBox="0 0 9 8"><rect y="0" width="9" height="1.5" fill="#fff"/><rect y="3.2" width="9" height="1.5" fill="#fff"/><rect y="6.4" width="9" height="1.5" fill="#fff"/></svg>
      </div>
      <h1 class="hero__title">REINVENTING RETIREMENT</h1>
      <p class="hero__text">The retirement village concept is still in its infancy in Southern Europe.<br>Retirement villages in North America, Australia and South Africa, for<br>example, have existed for some time.</p>
      <a class="btn btn--tour">VIRTUAL TOUR</a>
    </section>

    <section class="lead">
      <div class="lead__row">
        <div class="field field--third">Name :</div>
        <div class="field field--third">Email :</div>
        <div class="field field--third">Phone :</div>
      </div>
      <div class="lead__row">
        <div class="field field--half">Interest :</div>
        <div class="field field--half">Comment :</div>
      </div>
      <a class="btn btn--submit">SUBMIT</a>
    </section>

    <section class="videos">
      <div class="video">
        <div class="video__frame video__frame--aerial" role="img" aria-label="Aerial render of the development with pool and gardens"></div>
        <div class="video__play"><svg width="10" height="10" viewBox="0 0 10 10"><path d="M2 1 L9 5 L2 9 Z" fill="#fff"/></svg></div>
        <div class="video__bar"><span>▶</span><span class="video__time">0:00 / 3:00</span><span class="video__host">ClipHarbor</span></div>
      </div>
      <div class="video">
        <div class="video__frame video__frame--terrace" role="img" aria-label="Render of a rooftop terrace with sun loungers and sea view"></div>
        <div class="video__play"><svg width="10" height="10" viewBox="0 0 10 10"><path d="M2 1 L9 5 L2 9 Z" fill="#fff"/></svg></div>
        <div class="video__bar"><span>▶</span><span class="video__time">0:00 / 3:00</span><span class="video__host">ClipHarbor</span></div>
      </div>
    </section>

    <footer class="footer">© Copyright 2022 Brevoa Homes.All Rights Reserved</footer>
  </main>

</body>
</html>
```